Poster Design - Stand Up Paddle Eco Tour

We need a A3 size poster design (using Adobe Illustrator) for our company's stand up paddle tour. Our tour is on flat water, calm and safe, suitable for all ages and level.

WE provide worldclass SUP boards for our customers. And branded Tovar Helsby life jacket. Our instructors are all well trained and exeprience. Plus they are super friendly. Every paddling trip come with a safety boat.

Please refer to attached files for text and photos.

Our website is www.brimwakeglide.com.sg

IMPORTANT NOTE - The design has to be done in Adobe Illustrator. The winning designer has to submit the working file in Adobe Illustrator.

Target Market(s)

Working adult - 20 - 35 year old

Industry/Entity Type

Tourism

Requirements
Must have
• The project MUST be done in Adobe Illustrator and the winning designer has to submit the artwork to us in Adobe Illustrator format.
Nice to have
• pleasant to look at.

```html
<!DOCTYPE html>
<html lang="en">
<head>
<meta charset="utf-8">
<title>Brimwake Glide – SUP Eco Tour Poster</title>
<link rel="stylesheet" href="https://fonts.googleapis.com/css2?family=Oswald:wght@500;600&family=PT+Sans:wght@400;700&family=Montserrat:wght@700&family=Open+Sans:wght@300&display=swap">
<style>
  :root {
    --navy: #1d3450;
    --orange: #f29a2e;
    --sand: rgba(196, 140, 62, 0.88);
    --ink: #111;
    --white: #fff;
    --mist: #eef0f1;
    --mangrove-dark: #4d5f6e;
    --mangrove-mid: #8795a1;
    --water: #7fa6a3;
  }
  * { margin: 0; padding: 0; box-sizing: border-box; }
  html, body { width: 853px; height: 1200px; overflow: hidden; background: var(--white); }
  .poster {
    position: relative;
    width: 853px;
    height: 1200px;
    overflow: hidden;
    font-family: "PT Sans", sans-serif;
    background: var(--white);
  }
  .backdrop-scene {
    position: absolute;
    left: 0; top: 0;
    width: 853px; height: 1200px;
    background:
      linear-gradient(180deg, var(--white) 0%, var(--mist) 18%, #b9c2c9 30%, var(--mangrove-mid) 42%, var(--mangrove-dark) 62%, #56687a 80%, #6f7f8d 100%);
  }
  .brand {
    position: absolute;
    left: 32px; top: 62px;
    display: flex; align-items: center; gap: 8px;
    font-family: "Montserrat", sans-serif;
    font-weight: 700;
    font-size: 19px;
    color: var(--navy);
  }
  .brand-dot {
    width: 14px; height: 14px; border-radius: 50%;
    background: var(--navy);
  }
  .photo {
    position: absolute;
    border-radius: 50%;
    border: 6px solid var(--white);
  }
  .photo-river-group { left: 455px; top: 32px; width: 372px; height: 372px;
    background: linear-gradient(180deg, #cfe0ef 0%, #b7d0e6 22%, #3f6d3a 34%, #55794a 50%, #7c8f6e 70%, #8a9a7d 100%); }
  .photo-lineup { left: 596px; top: 494px; width: 212px; height: 212px;
    background: linear-gradient(180deg, #9fc6ea 0%, #d3e4f2 35%, #aec8c0 55%, #86b3ac 100%); }
  .photo-standing { left: 421px; top: 586px; width: 264px; height: 264px;
    background: linear-gradient(180deg, #3c5d32 0%, #4f7446 40%, #7c947d 60%, #8fa38a 100%); }
  .photo-open-water { left: 545px; top: 748px; width: 262px; height: 262px;
    background: linear-gradient(180deg, #a7cdee 0%, #d5e6f1 38%, #9ec3c0 50%, #7fb2ae 100%); }
  .headline {
    position: absolute; left: 32px; top: 278px;
    color: var(--ink);
  }
  .headline-lead {
    font-family: "Open Sans", sans-serif;
    font-weight: 300;
    font-size: 52px; line-height: 58px;
    letter-spacing: -1px;
  }
  .headline-sub {
    font-family: "Open Sans", sans-serif;
    font-weight: 300;
    font-size: 31px; line-height: 37px;
    letter-spacing: -0.5px;
  }
  .headline-feature {
    font-family: "Oswald", sans-serif;
    font-weight: 600;
    font-size: 45px; line-height: 58px;
    color: var(--orange);
    letter-spacing: 0.2px;
  }
  .intro {
    position: absolute; left: 32px; top: 582px; width: 400px;
    color: var(--white);
    font-size: 14px; line-height: 19px;
  }
  .callout {
    font-family: "Oswald", sans-serif;
    font-weight: 500;
    color: var(--orange);
  }
  .intro .callout { font-size: 21px; margin-top: 11px; }
  .guided {
    position: absolute; left: 32px; top: 786px; width: 380px;
    color: var(--white);
    font-size: 14px; line-height: 22px;
  }
  .guided .callout {
    font-family: "Montserrat", sans-serif;
    font-weight: 700;
    font-size: 21px; line-height: 25px;
    margin-bottom: 12px;
  }
  .info-band {
    position: absolute; left: 0; top: 1020px;
    width: 853px; height: 180px;
    background: var(--sand);
  }
  .info-block { position: absolute; color: var(--white); font-size: 14px; line-height: 18px; }
  .info-block h2 {
    font-family: "Montserrat", sans-serif;
    font-weight: 700;
    font-size: 19px; line-height: 24px;
    color: var(--navy);
  }
  .timing { left: 32px; top: 1040px; }
  .location { left: 32px; top: 1096px; width: 300px; }
  .booking { left: 428px; top: 1040px; }
  .booking-note { color: var(--navy); font-size: 17px; line-height: 22px; margin-top: 2px; }
  .contact-list { list-style: none; margin-top: 4px; }
  .contact-list li { display: flex; align-items: center; gap: 14px; font-size: 15px; line-height: 21px; padding-left: 12px; }
  .contact-list li::before {
    content: ""; width: 7px; height: 7px; border-radius: 50%;
    background: var(--orange); flex-shrink: 0;
  }
</style>
</head>
<body>
<main class="poster">
  <div class="backdrop-scene" role="img" aria-label="Faded blue-grey photograph of mangrove trees with a paddler standing on a board in the water"></div>

  <div class="brand"><span class="brand-dot"></span>Brimwake Glide</div>

  <div class="photo photo-river-group" role="img" aria-label="Photo of a group of paddlers on boards on a calm green river between mangroves"></div>
  <div class="photo photo-lineup" role="img" aria-label="Photo of a line of paddlers sitting on boards on open water"></div>
  <div class="photo photo-standing" role="img" aria-label="Photo of two paddlers standing on yellow boards near mangroves"></div>
  <div class="photo photo-open-water" role="img" aria-label="Photo of paddlers spread across wide open calm water"></div>

  <h1 class="headline">
    <span class="headline-lead">Explore</span><br>
    <span class="headline-sub">the natural coastal surroundings<br>and waterways of Johor on a</span><br>
    <span class="headline-feature">SUP Adventure Touring Board</span>
  </h1>

  <section class="intro">
    <p>Our tours are flat-water and appropriate for all ages and levels.<br>We have the best possible service and equipment.</p>
    <p class="callout">Join us for a fun and relaxing day</p>
  </section>

  <section class="guided">
    <h2 class="callout">What could be better than<br>a group guided tour?</h2>
    <p>With life vests and a safety boat for our guided tour, you can be assured of a secured environment while you focus on just having funand creating life's best memories with friends and family.</p>
  </section>

  <div class="info-band"></div>

  <section class="info-block timing">
    <h2>Timing</h2>
    <p>Morning, afternoon, and sunset session</p>
  </section>

  <section class="info-block location">
    <h2>Location</h2>
    <p>Sungai Lembah, set off from Teluk Seroja,<br>Tanjung Merah. (next to Pantai Seri)</p>
  </section>

  <section class="info-block booking">
    <h2>Contact us for booking</h2>
    <p class="booking-note">We do not accept walk-in</p>
    <ul class="contact-list">
      <li>+65-61234870</li>
      <li>www.brimwakeglide.com.sg</li>
      <li>social: brimwakeglide</li>
      <li>booking@brimwakeglide.com.sg</li>
    </ul>
  </section>
</main>
</body>
</html>
```